Tolvik cards

I want a simple business card that pops.
Logo on one side.
On side two i want.
"Are you thinking about a new building on your property, or renovating an existing structure? Contact".....
Owners Name: Gary Pellman
Owners Phone number: 555-209-4176
Address:4716 Copper Fern RD, Marlow Springs, PA 10478
Committed to Quality, Service, and Integrity

```html
<!DOCTYPE html>
<html lang="en">
<head>
<meta charset="utf-8">
<title>Tolvik Builders LLC – Business Card</title>
<link rel="stylesheet" href="https://fonts.googleapis.com/css2?family=Montserrat:wght@400;500;700&display=swap">
<style>
  :root {
    --backdrop: #e8e6e2;
    --card-white: #ffffff;
    --brand-brown: #3f2e1d;
    --ink: #2a1f15;
    --reverse-ink: #ffffff;
  }
  * { margin: 0; padding: 0; box-sizing: border-box; }
  html, body {
    width: 1181px;
    height: 1200px;
    overflow: hidden;
    background: var(--backdrop);
    font-family: "Montserrat", sans-serif;
    color: var(--ink);
  }
  .canvas {
    position: relative;
    width: 1181px;
    height: 1200px;
  }
  .card {
    position: absolute;
    left: 221px;
    width: 744px;
    height: 425px;
    box-shadow: 0 10px 28px rgba(0, 0, 0, 0.18);
  }
  .card-front { top: 126px; background: var(--card-white); }
  .card-back {
    top: 657px;
    background: var(--brand-brown);
    display: flex;
    align-items: center;
    justify-content: center;
  }
  .owner-name {
    position: absolute;
    left: 27px;
    top: 74px;
    font-size: 27px;
    font-weight: 500;
    color: var(--brand-brown);
    letter-spacing: 0.2px;
  }
  .owner-name .first { font-weight: 700; }
  .tagline {
    position: absolute;
    left: 27px;
    top: 118px;
    font-size: 13px;
    font-weight: 400;
    color: var(--ink);
  }
  .divider {
    position: absolute;
    left: 27px;
    top: 169px;
    width: 420px;
    height: 2px;
    background: var(--brand-brown);
  }
  .contact-row {
    position: absolute;
    left: 27px;
    display: flex;
    align-items: center;
    gap: 15px;
    font-size: 22px;
    font-weight: 400;
  }
  .contact-phone { top: 206px; }
  .contact-address { top: 247px; }
  .contact-icon { width: 26px; height: 26px; flex: none; }
  .pitch {
    position: absolute;
    left: 27px;
    top: 296px;
    width: 700px;
    font-size: 22px;
    line-height: 30px;
    font-weight: 400;
  }
  .brand-name {
    position: absolute;
    right: 30px;
    top: 92px;
    font-size: 22px;
    font-weight: 700;
    color: var(--brand-brown);
    letter-spacing: 0.5px;
    text-transform: uppercase;
  }
  .brand-name-reverse {
    font-size: 34px;
    font-weight: 700;
    color: var(--reverse-ink);
    letter-spacing: 1px;
    text-transform: uppercase;
  }
</style>
</head>
<body>
<main class="canvas">
  <section class="card card-front">
    <h1 class="owner-name"><span class="first">Gary</span> Pellman</h1>
    <p class="tagline">Committed to Quality, Service, and Integrity</p>
    <div class="divider"></div>

    <p class="contact-row contact-phone">
      <svg class="contact-icon" viewBox="0 0 26 26" aria-hidden="true">
        <circle cx="13" cy="13" r="13" fill="var(--brand-brown)"/>
        <path d="M9.2 6.5c.5-.3 1.1-.1 1.4.4l1.2 2.3c.2.5.1 1-.3 1.3l-1 .8c.7 1.6 1.9 2.9 3.5 3.7l.8-1c.3-.4.9-.5 1.3-.3l2.3 1.2c.5.3.7.9.4 1.4l-.7 1.3c-.4.7-1.2 1.1-2 .9-4-1-7.2-4.2-8.1-8.2-.2-.8.2-1.6.9-2z" fill="#fff"/>
      </svg>
      <span>555-209-4176</span>
    </p>

    <p class="contact-row contact-address">
      <svg class="contact-icon" viewBox="0 0 26 26" aria-hidden="true">
        <path d="M13 1.5c-5 0-8.8 3.8-8.8 8.6 0 6.2 8.8 14.4 8.8 14.4s8.8-8.2 8.8-14.4c0-4.8-3.8-8.6-8.8-8.6z" fill="var(--brand-brown)"/>
        <circle cx="13" cy="10" r="3.4" fill="#fff"/>
      </svg>
      <span>4716 Copper Fern RD, Marlow Springs, PA 10478</span>
    </p>

    <p class="pitch">Are you thinking about a new building on your property, or renovating an existing structure? Contact</p>

    <p class="brand-name">Tolvik Builders LLC</p>
  </section>

  <section class="card card-back">
    <p class="brand-name-reverse">Tolvik</p>
  </section>
</main>
</body>
</html>
```